Design personal page for IT Expert

I'm freelancer in the area of IT Architecture/Cloud Computing/DevOps. <br/>Already have own page: www.dremtova.cc<br/><br/>I want to update/redesign it and have following sections/pages there:<br/>1) My short bio/details/soft skills<br/>2) List of my hard skills<br/>3) My key clients/success stories/feedbacks<br/>4) List of my conference talks with links/embedded youtube video<br/>5) List of my articles with links (probably article text on sub-page like blog)<br/><br/>Design should be compatible with wix.com (gona have premium plan there)<br/>

Number of Pages Required

4 page

Font styles to use
Sans Serif

Colors

Designer to choose colors to be used in the design.

Requirements
Must have
• 1) My short bio/details/soft skills
• 2) List of my hard skills
• 3) My key clients/success stories/feedbacks
• 4) List of my conference talks with links/embedded youtube video
• 5) List of my articles with links (probably article text on sub-page like blog)
Should not have
• No direct contact to my skype/email. I prefer to use this platform for my task discussion.

```html
<!DOCTYPE html>
<html lang="en">
<head>
<meta charset="utf-8">
<title>Resume – Pavel Dremtov</title>
<link href="https://fonts.googleapis.com/css2?family=Playfair+Display:wght@700&family=Poppins:wght@400;500;600;700&display=swap" rel="stylesheet">
<style>
:root{
  --sidebar:#2e2e2e;
  --sidebar-line:#3a3a3a;
  --page:#f9f9f9;
  --card:#ffffff;
  --card-border:#ececec;
  --accent:#f47c5c;
  --ink:#2b2b2b;
  --muted:#555555;
  --faint:#9a9a9a;
  --white:#ffffff;
}
*{box-sizing:border-box;margin:0;padding:0}
html,body{width:1102px;height:1200px;overflow:hidden}
body{font-family:"Poppins",sans-serif;background:var(--page);color:var(--ink);position:relative}

.sidebar{position:absolute;left:0;top:0;width:217px;height:1200px;background:var(--sidebar);color:var(--white);text-align:center}
.avatar{position:absolute;left:68px;top:55px;width:83px;height:83px;border-radius:50%;border:3px solid #5a5a5a;background:radial-gradient(circle at 50% 40%,#e9c3ab 0%,#c99a80 45%,#4a3a36 80%)}
.profile-name{position:absolute;top:155px;width:100%;font-size:12.5px;font-weight:700}
.profile-role{position:absolute;top:178px;width:100%;font-size:8.8px;line-height:18px;color:#e8e8e8}
.divider{position:absolute;left:42px;width:134px;height:1px;background:var(--sidebar-line)}
.nav{position:absolute;top:0;left:0;width:100%;list-style:none}
.nav li{position:absolute;width:100%;font-size:10.6px;font-weight:500;text-transform:uppercase}
.nav li.active span{color:var(--accent);border-bottom:1px solid var(--accent);padding-bottom:1px}
.connect{position:absolute;top:549px;width:100%;font-size:9px;color:#e8e8e8}
.socials{position:absolute;top:571px;width:100%;display:flex;justify-content:center;gap:10px;font-size:8px;color:#cfcfcf}
.socials span{display:flex;align-items:center;gap:3px}
.socials i{display:block;width:12px;height:12px;background:#474747}
.rights{position:absolute;top:1177px;width:100%;font-size:8px;color:#6d6d6d;text-transform:uppercase}

.page-title{position:absolute;left:217px;right:0;top:72px;text-align:center;font-family:"Playfair Display",serif;font-size:30px;color:var(--ink)}
.title-rule{position:absolute;height:2px;background:#e6e6e6}
.section-label{position:absolute;font-size:10.5px;font-weight:500;color:var(--ink);border-bottom:1.5px solid var(--accent);line-height:14px}
.download{position:absolute;left:913px;top:173px;width:118px;height:34px;background:var(--accent);color:var(--white);font-size:9.5px;font-weight:700;display:flex;align-items:center;justify-content:center;text-transform:uppercase}

.timeline{position:absolute;top:227px;width:362px;height:517px;border-left:1.5px solid var(--accent)}
.entry{position:absolute;left:21px;width:340px;height:114px;background:var(--card);border:1px solid var(--card-border);padding:18px 8px 18px 20px}
.entry svg.marker{position:absolute;left:-22px;top:22px}
.entry-date{display:flex;align-items:center;gap:7px;font-size:9px;color:var(--accent)}
.entry-title{margin-top:12px;font-size:10.5px;font-weight:500;color:var(--ink)}
.entry-text{margin-top:4px;font-size:8.4px;letter-spacing:-0.15px;line-height:16.5px;color:var(--muted);white-space:nowrap}

.skills{position:absolute;top:835px}
.skill{position:absolute;left:0;width:100%}
.skill-head{display:flex;justify-content:space-between;align-items:baseline}
.skill-name{font-size:9.3px;font-weight:500;color:var(--ink)}
.skill-pct{font-size:7.5px;color:var(--faint)}
.bar{margin-top:3px;height:7px;border:1px solid var(--accent);border-radius:4px;padding:1px 2px}
.bar i{display:block;height:3px;width:87%;background:var(--accent);border-radius:2px}
.skill-list{margin-top:7px;text-align:center;font-size:8.2px;color:var(--muted);white-space:nowrap}
</style>
</head>
<body>

<aside class="sidebar">
  <div class="avatar" role="img" aria-label="Portrait photo of Pavel Dremtov"></div>
  <div class="profile-name">Pavel Dremtov</div>
  <div class="profile-role">-Cloud DevOps &amp; Architect<br>-CI/CD Automation Expert</div>
  <div class="divider" style="top:250px"></div>
  <ul class="nav">
    <li style="top:289px"><span>Home</span></li>
    <li style="top:324px"><span>About Me</span></li>
    <li class="active" style="top:357px"><span>Hard Skills</span></li>
    <li style="top:389px"><span>Successful Stories</span></li>
    <li style="top:422px"><span>Conference Talks</span></li>
    <li style="top:456px"><span>Articles/Blog</span></li>
  </ul>
  <div class="divider" style="top:511px"></div>
  <div class="connect">Connect With Me:</div>
  <div class="socials"><span><i></i>Pulse</span><span><i></i>Nexo</span></div>
  <div class="rights">All Rights Reserved</div>
</aside>

<main>
  <h1 class="page-title">Resume</h1>
  <div class="title-rule" style="left:590px;top:111px;width:138px"></div>
  <div class="title-rule" style="left:625px;top:117px;width:69px"></div>

  <div class="section-label" style="left:289px;top:170px">Education</div>
  <div class="section-label" style="left:670px;top:170px">Experience</div>
  <div class="download">Download CV</div>

  <section class="timeline" style="left:289px">
    <article class="entry" style="top:0"><svg class="marker" width="22" height="10"><path d="M0 0L8 5L0 10Z" fill="#f47c5c"/><line x1="8" y1="5" x2="22" y2="5" stroke="#f47c5c"/></svg><div class="entry-date"><svg width="11" height="11" viewBox="0 0 11 11"><rect x="0.5" y="1.5" width="10" height="9" fill="none" stroke="#f47c5c"/><line x1="0.5" y1="4" x2="10.5" y2="4" stroke="#f47c5c"/><line x1="3" y1="0" x2="3" y2="2.5" stroke="#f47c5c"/><line x1="8" y1="0" x2="8" y2="2.5" stroke="#f47c5c"/></svg>2004-2006</div><div class="entry-title">Lorem Ipsum Dolor Amet</div><p class="entry-text">Lorem ipsum dolor sit amet, consectetur adipiscing elit. Integermat<br>fermentum nibh et metus facilisis sollicitudin</p></article>
    <article class="entry" style="top:134px"><svg class="marker" width="22" height="10"><path d="M0 0L8 5L0 10Z" fill="#f47c5c"/><line x1="8" y1="5" x2="22" y2="5" stroke="#f47c5c"/></svg><div class="entry-date"><svg width="11" height="11" viewBox="0 0 11 11"><rect x="0.5" y="1.5" width="10" height="9" fill="none" stroke="#f47c5c"/><line x1="0.5" y1="4" x2="10.5" y2="4" stroke="#f47c5c"/><line x1="3" y1="0" x2="3" y2="2.5" stroke="#f47c5c"/><line x1="8" y1="0" x2="8" y2="2.5" stroke="#f47c5c"/></svg>2004-2006</div><div class="entry-title">Lorem Ipsum Dolor Amet</div><p class="entry-text">Lorem ipsum dolor sit amet, consectetur adipiscing elit. Integermat<br>fermentum nibh et metus facilisis sollicitudin</p></article>
    <article class="entry" style="top:268px"><svg class="marker" width="22" height="10"><path d="M0 0L8 5L0 10Z" fill="#f47c5c"/><line x1="8" y1="5" x2="22" y2="5" stroke="#f47c5c"/></svg><div class="entry-date"><svg width="11" height="11" viewBox="0 0 11 11"><rect x="0.5" y="1.5" width="10" height="9" fill="none" stroke="#f47c5c"/><line x1="0.5" y1="4" x2="10.5" y2="4" stroke="#f47c5c"/><line x1="3" y1="0" x2="3" y2="2.5" stroke="#f47c5c"/><line x1="8" y1="0" x2="8" y2="2.5" stroke="#f47c5c"/></svg>2004-2006</div><div class="entry-title">Lorem Ipsum Dolor Amet</div><p class="entry-text">Lorem ipsum dolor sit amet, consectetur adipiscing elit. Integermat<br>fermentum nibh et metus facilisis sollicitudin</p></article>
    <article class="entry" style="top:403px"><svg class="marker" width="22" height="10"><path d="M0 0L8 5L0 10Z" fill="#f47c5c"/><line x1="8" y1="5" x2="22" y2="5" stroke="#f47c5c"/></svg><div class="entry-date"><svg width="11" height="11" viewBox="0 0 11 11"><rect x="0.5" y="1.5" width="10" height="9" fill="none" stroke="#f47c5c"/><line x1="0.5" y1="4" x2="10.5" y2="4" stroke="#f47c5c"/><line x1="3" y1="0" x2="3" y2="2.5" stroke="#f47c5c"/><line x1="8" y1="0" x2="8" y2="2.5" stroke="#f47c5c"/></svg>2004-2006</div><div class="entry-title">Lorem Ipsum Dolor Amet</div><p class="entry-text">Lorem ipsum dolor sit amet, consectetur adipiscing elit. Integermat<br>fermentum nibh et metus facilisis sollicitudin</p></article>
  </section>

  <section class="timeline" style="left:671px">
    <article class="entry" style="top:0"><svg class="marker" width="22" height="10"><path d="M0 0L8 5L0 10Z" fill="#f47c5c"/><line x1="8" y1="5" x2="22" y2="5" stroke="#f47c5c"/></svg><div class="entry-date"><svg width="11" height="11" viewBox="0 0 11 11"><rect x="0.5" y="1.5" width="10" height="9" fill="none" stroke="#f47c5c"/><line x1="0.5" y1="4" x2="10.5" y2="4" stroke="#f47c5c"/><line x1="3" y1="0" x2="3" y2="2.5" stroke="#f47c5c"/><line x1="8" y1="0" x2="8" y2="2.5" stroke="#f47c5c"/></svg>2004-2006</div><div class="entry-title">Lorem Ipsum Dolor Amet</div><p class="entry-text">Lorem ipsum dolor sit amet, consectetur adipiscing elit. Integermat<br>fermentum nibh et metus facilisis sollicitudin</p></article>
    <article class="entry" style="top:134px"><svg class="marker" width="22" height="10"><path d="M0 0L8 5L0 10Z" fill="#f47c5c"/><line x1="8" y1="5" x2="22" y2="5" stroke="#f47c5c"/></svg><div class="entry-date"><svg width="11" height="11" viewBox="0 0 11 11"><rect x="0.5" y="1.5" width="10" height="9" fill="none" stroke="#f47c5c"/><line x1="0.5" y1="4" x2="10.5" y2="4" stroke="#f47c5c"/><line x1="3" y1="0" x2="3" y2="2.5" stroke="#f47c5c"/><line x1="8" y1="0" x2="8" y2="2.5" stroke="#f47c5c"/></svg>2004-2006</div><div class="entry-title">Lorem Ipsum Dolor Amet</div><p class="entry-text">Lorem ipsum dolor sit amet, consectetur adipiscing elit. Integermat<br>fermentum nibh et metus facilisis sollicitudin</p></article>
    <article class="entry" style="top:268px"><svg class="marker" width="22" height="10"><path d="M0 0L8 5L0 10Z" fill="#f47c5c"/><line x1="8" y1="5" x2="22" y2="5" stroke="#f47c5c"/></svg><div class="entry-date"><svg width="11" height="11" viewBox="0 0 11 11"><rect x="0.5" y="1.5" width="10" height="9" fill="none" stroke="#f47c5c"/><line x1="0.5" y1="4" x2="10.5" y2="4" stroke="#f47c5c"/><line x1="3" y1="0" x2="3" y2="2.5" stroke="#f47c5c"/><line x1="8" y1="0" x2="8" y2="2.5" stroke="#f47c5c"/></svg>2004-2006</div><div class="entry-title">Lorem Ipsum Dolor Amet</div><p class="entry-text">Lorem ipsum dolor sit amet, consectetur adipiscing elit. Integermat<br>fermentum nibh et metus facilisis sollicitudin</p></article>
    <article class="entry" style="top:403px"><svg class="marker" width="22" height="10"><path d="M0 0L8 5L0 10Z" fill="#f47c5c"/><line x1="8" y1="5" x2="22" y2="5" stroke="#f47c5c"/></svg><div class="entry-date"><svg width="11" height="11" viewBox="0 0 11 11"><rect x="0.5" y="1.5" width="10" height="9" fill="none" stroke="#f47c5c"/><line x1="0.5" y1="4" x2="10.5" y2="4" stroke="#f47c5c"/><line x1="3" y1="0" x2="3" y2="2.5" stroke="#f47c5c"/><line x1="8" y1="0" x2="8" y2="2.5" stroke="#f47c5c"/></svg>2004-2006</div><div class="entry-title">Lorem Ipsum Dolor Amet</div><p class="entry-text">Lorem ipsum dolor sit amet, consectetur adipiscing elit. Integermat<br>fermentum nibh et metus facilisis sollicitudin</p></article>
  </section>

  <div class="section-label" style="left:632px;top:783px">Hard Skills</div>

  <section class="skills" style="left:296px;width:354px">
    <div class="skill" style="top:0"><div class="skill-head"><span class="skill-name">Cloud Providers</span><span class="skill-pct">80%</span></div><div class="bar"><i></i></div><p class="skill-list">Nimbra Web Services, Skyloft Cloud Platform, Postvik Cloud, Openrig Cloud</p></div>
    <div class="skill" style="top:62px"><div class="skill-head"><span class="skill-name">Norix Fundamentals</span><span class="skill-pct">80%</span></div><div class="bar"><i></i></div><p class="skill-list">Nimbra Norix/Dervan/Ubira, Shell Scripting, Firewalls, Networking, Protocols TCP/UDP</p></div>
    <div class="skill" style="top:127px"><div class="skill-head"><span class="skill-name">CI/CD</span><span class="skill-pct">80%</span></div><div class="bar"><i></i></div><p class="skill-list">Collect &amp; Plan Requirements, Fetch Code, Build App Modules, Release Versioning, etc</p></div>
    <div class="skill" style="top:186px"><div class="skill-head"><span class="skill-name">Monitoring</span><span class="skill-pct">80%</span></div><div class="bar"><i></i></div><p class="skill-list">Metrion, Gaugely, NWS Cloud Eye, Zentro, Logwell, Streamlet, Searchly - Viewpane</p></div>
    <div class="skill" style="top:244px"><div class="skill-head"><span class="skill-name">Coding Languages</span><span class="skill-pct">80%</span></div><div class="bar"><i></i></div><p class="skill-list">Jorvo, Pyra 2/3, Shell, Nodal JS, Gox, C/C++</p></div>
  </section>

  <section class="skills" style="left:693px;width:338px">
    <div class="skill" style="top:0"><div class="skill-head"><span class="skill-name">Configuration Managment</span><span class="skill-pct">80%</span></div><div class="bar"><i></i></div><p class="skill-list" style="margin-top:4px">Landplan, StackForm, Provisio, Boxwell, Stringer</p></div>
    <div class="skill" style="top:65px"><div class="skill-head"><span class="skill-name">Tools</span><span class="skill-pct">80%</span></div><div class="bar"><i></i></div><p class="skill-list" style="margin-top:4px">Tasko, Packlo, Stepper, Builda, Grainly, Forgex, Rudder, Modu</p></div>
    <div class="skill" style="top:127px"><div class="skill-head"><span class="skill-name">Load Balancing</span><span class="skill-pct">80%</span></div><div class="bar"><i></i></div><p class="skill-list">NWS Network Load Balancer, NWS Application Load Balancer, FlowGate, Portwise</p></div>
    <div class="skill" style="top:186px"><div class="skill-head"><span class="skill-name">Integration</span><span class="skill-pct">80%</span></div><div class="bar"><i></i></div><p class="skill-list">RelayCI, LoopCI, RepoCI, Shipwise, Quadrix, Canebuild, CrewCity, Steward</p></div>
    <div class="skill" style="top:244px"><div class="skill-head"><span class="skill-name">Data</span><span class="skill-pct">80%</span></div><div class="bar"><i></i></div><p class="skill-list">TableSeek, Dawnbase, Keystash, LeafDoc, TideStore, Streamline/Quorum, Widecol</p></div>
  </section>
</main>

</body>
</html>
```